hair salon business Card Design

My business name is Hair & Beauty @ Corvale I want a Hot Pink and black business card with a loyalty program on the back after every 2nd haircut the third has $5 off and I will whole punch the squares My business phone number is (07) 58 913 640 address is Shop 4 3/9 Brambury st Corvale Qld 4570 find us on facebook should be on the card somewhere with the facebook logo also a space alocated for your next appointment date n time also would like your har stylists name is Tez on the card somewhere easy to read you can check out my facebook site for images of my logo n shop signage

Industry/Entity Type

Hair

```html
<!DOCTYPE html>
<html lang="en">
<head>
<meta charset="utf-8">
<title>Hair &amp; Beauty @ Corvale – Appointment Card</title>
<link rel="stylesheet" href="https://fonts.googleapis.com/css2?family=Questrial&family=Nunito:ital,wght@0,800;1,900&family=Courgette&display=swap">
<style>
  :root {
    --pink-light: #f246ea;
    --pink: #e313d3;
    --pink-deep: #b8009f;
    --lilac: #f5cdf3;
    --white: #ffffff;
    --ink: #1f2121;
    --charcoal: #2f3434;
    --charcoal-dark: #1e2222;
    --text-light: #eef0f0;
    --rule: #c9a6c6;
  }
  * { margin: 0; padding: 0; box-sizing: border-box; }
  html, body {
    width: 1200px; height: 741px; overflow: hidden; background: #ffffff;
  }
  .card {
    position: relative; width: 1200px; height: 741px; overflow: hidden;
    font-family: "Questrial", sans-serif;
  }
  .card__face {
    position: absolute; inset: 0 0 190px 0;
    background:
      radial-gradient(ellipse 60% 70% at 85% 30%, rgba(255,255,255,0.12), transparent 70%),
      radial-gradient(ellipse 45% 60% at 8% 35%, rgba(255,255,255,0.10), transparent 70%),
      linear-gradient(180deg, var(--pink-light) 0%, var(--pink) 55%, var(--pink-deep) 100%);
  }
  .brand {
    position: absolute; left: 0; right: 0; top: 70px;
    text-align: center; color: var(--white); font-weight: 400;
    font-family: "Questrial", sans-serif;
  }
  .brand__name { font-size: 112px; line-height: 1; letter-spacing: 1px; }
  .brand__place { font-size: 74px; line-height: 1; margin-top: 8px; letter-spacing: 2px; }

  .appointment {
    position: absolute; left: 231px; top: 296px; width: 725px; height: 228px;
    box-shadow: 0 2px 6px rgba(0,0,0,0.25);
  }
  .appointment__header {
    height: 80px; background: var(--ink); position: relative;
  }
  .appointment__lead {
    position: absolute; left: 17px; top: 8px;
    font-family: "Nunito", sans-serif; font-style: italic; font-weight: 900;
    font-size: 36px; color: var(--pink); letter-spacing: 0.5px;
  }
  .appointment__title {
    position: absolute; left: 95px; top: 30px;
    font-family: "Courgette", cursive; font-size: 36px; color: var(--white);
  }
  .appointment__row {
    display: grid; grid-template-columns: 79px 211px 211px 224px;
  }
  .appointment__row--date { height: 73px; background: var(--white); }
  .appointment__row--time { height: 75px; background: var(--lilac); }
  .appointment__cell { border-left: 2px solid var(--rule); position: relative; }
  .appointment__icon {
    border-left: none; display: flex; align-items: center; justify-content: center;
  }
  .appointment__meridiem {
    position: absolute; right: 20px; top: 8px; text-align: right;
    font-family: "Nunito", sans-serif; font-weight: 800; font-size: 27px;
    line-height: 31px; color: var(--ink);
  }

  .contact {
    position: absolute; left: 0; right: 0; bottom: 0; height: 190px;
    background: linear-gradient(180deg, var(--charcoal) 0%, var(--charcoal-dark) 100%);
  }
  .contact__tube {
    position: absolute; left: 67px; top: -18px; width: 63px; height: 220px;
    border-radius: 14px 14px 0 0;
    background: linear-gradient(90deg, #9ea2a4 0%, #ffffff 40%, #e4e6e7 65%, #7d8284 100%);
  }
  .contact__line {
    position: absolute; left: 159px; font-size: 39px; color: var(--text-light);
    letter-spacing: 0.5px; white-space: nowrap;
  }
  .contact__line--phone { top: 23px; }
  .contact__line--address { top: 82px; }
  .contact__badge { position: absolute; left: 75px; width: 40px; height: 40px; }
  .contact__badge--phone { top: 25px; }
  .contact__badge--address { top: 84px; }
</style>
</head>
<body>
<main class="card">
  <section class="card__face">
    <h1 class="brand">
      <div class="brand__name">Hair &amp; Beauty</div>
      <div class="brand__place">@CORVALE</div>
    </h1>

    <div class="appointment">
      <div class="appointment__header">
        <span class="appointment__lead">your next</span>
        <span class="appointment__title">appointment</span>
      </div>
      <div class="appointment__row appointment__row--date">
        <div class="appointment__cell appointment__icon">
          <svg width="44" height="44" viewBox="0 0 44 44" aria-label="Date">
            <rect x="3" y="6" width="38" height="35" rx="5" fill="#1f2121"/>
            <rect x="11" y="1" width="5" height="10" rx="2" fill="#1f2121"/>
            <rect x="28" y="1" width="5" height="10" rx="2" fill="#1f2121"/>
            <g fill="#ffffff">
              <rect x="8" y="18" width="6" height="5"/><rect x="16" y="18" width="6" height="5"/><rect x="24" y="18" width="6" height="5"/><rect x="32" y="18" width="5" height="5"/>
              <rect x="8" y="26" width="6" height="5"/><rect x="16" y="26" width="6" height="5"/><rect x="24" y="26" width="6" height="5"/><rect x="32" y="26" width="5" height="5"/>
              <rect x="8" y="33" width="6" height="5"/><rect x="16" y="33" width="6" height="5"/><rect x="24" y="33" width="6" height="5"/>
            </g>
          </svg>
        </div>
        <div class="appointment__cell"></div>
        <div class="appointment__cell"></div>
        <div class="appointment__cell"></div>
      </div>
      <div class="appointment__row appointment__row--time">
        <div class="appointment__cell appointment__icon">
          <svg width="48" height="48" viewBox="0 0 48 48" aria-label="Time">
            <circle cx="24" cy="24" r="20" fill="#ffffff" stroke="#1f2121" stroke-width="4"/>
            <path d="M24 11 V25 H33" fill="none" stroke="#1f2121" stroke-width="4" stroke-linecap="round"/>
          </svg>
        </div>
        <div class="appointment__cell"><div class="appointment__meridiem">pm<br>am</div></div>
        <div class="appointment__cell"><div class="appointment__meridiem">pm<br>am</div></div>
        <div class="appointment__cell"><div class="appointment__meridiem">pm<br>am</div></div>
      </div>
    </div>
  </section>

  <footer class="contact">
    <div class="contact__tube"></div>
    <svg class="contact__badge contact__badge--phone" viewBox="0 0 40 40" aria-label="Phone">
      <circle cx="20" cy="20" r="19" fill="#e313d3" stroke="#ffffff" stroke-width="1.5"/>
      <path d="M14 10 l4 0 l2 6 l-3 2 q2 5 6 7 l2 -3 l6 2 l0 4 q-1 3 -4 3 q-9 -1 -15 -12 q-1 -6 2 -9z" fill="#ffffff"/>
    </svg>
    <div class="contact__line contact__line--phone">(07) 58 913 640</div>
    <svg class="contact__badge contact__badge--address" viewBox="0 0 40 40" aria-label="Address">
      <circle cx="20" cy="20" r="19" fill="#e313d3" stroke="#ffffff" stroke-width="1.5"/>
      <path d="M8 21 L20 10 L32 21 H28 V30 H23 V24 H17 V30 H12 V21 Z" fill="#ffffff"/>
    </svg>
    <div class="contact__line contact__line--address">Shop 4 3/9 Brambury st Corvale Qld 4570</div>
  </footer>
</main>
</body>
</html>
```